plumbing & gas fitting business card design

We need a business card design for a plumbing & gas fitting company. The company covers commercial, domestic and maintenance work. We would like a modern design communicating efficiency and sophistication. preferred colours would include (red grey & black) or (green grey & black). Please DO NOT include any water droplets.

Industry/Entity Type

Business

Contact Information for Business Card

Vortig Plumbing & Gas, Commercial Domestic & Maintenance, licence no. 617394K, ABN 47215830962, Phone 0417382956, Email vortigplumbingandgas@corvanet.com

```html
<!DOCTYPE html>
<html lang="en">
<head>
<meta charset="utf-8">
<title>Vortig Plumbing &amp; Gas – Business Card</title>
<link rel="stylesheet" href="https://fonts.googleapis.com/css2?family=Cormorant+Garamond:wght@500;600&display=swap">
<style>
  :root {
    --green: #338b6a;
    --ink: #231f20;
    --grey: #7a7a7c;
    --paper: #ffffff;
    --edge: #c9c9c9;
    --backdrop: #ffffff;
  }
  html, body {
    margin: 0;
    width: 1200px;
    height: 1000px;
    overflow: hidden;
    background: var(--backdrop);
  }
  .card {
    position: absolute;
    left: 45px;
    top: 185px;
    width: 1107px;
    height: 632px;
    background: var(--paper);
    border: 1px solid var(--edge);
    box-sizing: border-box;
    overflow: hidden;
    font-family: "Cormorant Garamond", Georgia, serif;
  }
  .brand-name {
    position: absolute;
    left: 327px;
    top: 78px;
    margin: 0;
    font-size: 86px;
    font-weight: 500;
    line-height: 1;
    letter-spacing: 0.26em;
    color: var(--green);
  }
  .brand-trade {
    position: absolute;
    left: 328px;
    top: 176px;
    margin: 0;
    font-size: 50px;
    font-weight: 500;
    line-height: 1;
    letter-spacing: 0.2em;
    color: var(--ink);
    white-space: nowrap;
  }
  .brand-trade .amp { color: var(--grey); }
  .service-band {
    position: absolute;
    left: 235px;
    right: 0;
    top: 278px;
    height: 39px;
    background: var(--green);
    color: var(--paper);
    display: flex;
    align-items: center;
    padding-left: 100px;
    font-size: 27px;
    font-weight: 500;
    letter-spacing: 0.06em;
    white-space: nowrap;
  }
  .service-band .divider {
    display: inline-block;
    width: 1px;
    height: 26px;
    background: rgba(255,255,255,0.7);
    margin: 0 14px;
  }
  .contact-list {
    position: absolute;
    left: 300px;
    width: 710px;
    top: 362px;
    margin: 0;
    padding: 0;
    list-style: none;
    text-align: center;
  }
  .contact-list li {
    height: 55px;
    line-height: 55px;
    white-space: nowrap;
  }
  .contact-label {
    color: var(--green);
    font-size: 25px;
    font-weight: 500;
    letter-spacing: 0.08em;
    margin-right: 8px;
  }
  .contact-value {
    color: var(--ink);
    font-size: 32px;
    font-weight: 500;
    letter-spacing: 0.04em;
  }
  .contact-value.email { font-size: 30px; letter-spacing: 0.01em; }
</style>
</head>
<body>
  <main class="card">
    <h1 class="brand-name">VORTIG</h1>
    <p class="brand-trade">PLUMBING <span class="amp">&amp;</span> GAS</p>

    <div class="service-band">
      <span>COMMERCIAL</span><span class="divider"></span><span>DOMESTIC</span><span class="divider"></span><span>MAINTENANCE</span>
    </div>

    <ul class="contact-list">
      <li><span class="contact-label">LICENCE NO.</span><span class="contact-value">617394K</span></li>
      <li><span class="contact-label">ABN</span><span class="contact-value">47215830962</span></li>
      <li><span class="contact-label">PHONE</span><span class="contact-value">0417382956</span></li>
      <li><span class="contact-label">EMAIL</span><span class="contact-value email">vortigplumbingandgas@corvanet.com</span></li>
    </ul>
  </main>
</body>
</html>
```